The (Private) News Sharing Report

This is a professional and academic report of 35 pages for journalists and teachers. The topic of the report is News Sharing: journalism, social networks and technology. Attached there is an example of the kind of design we are looking for: visual, fresh and modern.

Target Market(s)

Journalists, Journalism Students, Communication Researchers,

Industry/Entity Type

Media

Font styles to use
Sans Serif

Colors
3276b5
33a6d7
886aae
b868aa

Requirements
Must have
• Copyleft images, visual style
Nice to have
• There is an example attached.

```html
<!DOCTYPE html>
<html lang="en">
<head>
<meta charset="utf-8">
<title>The (Private) News Sharing Report – Layout Presentation</title>
<link href="https://fonts.googleapis.com/css2?family=Montserrat:wght@400;600;700;800&family=Roboto:ital,wght@0,400;0,500;0,700;1,400&display=swap" rel="stylesheet">
<style>
:root{
  --stage:#3a3a3a;
  --board:#c9c9c9;
  --ink:#2b2b2b;
  --text:#3d3d3d;
  --sky:#4cb1e1;
  --sky-light:#a9daf2;
  --sky-deep:#2f8fd2;
  --heading:#2a8fd4;
  --band:#e6e6e6;
  --band-dark:#d9d9d9;
  --white:#ffffff;
  --art-a:#8a6caf;
  --art-b:#33a6d7;
}
*{box-sizing:border-box;margin:0;padding:0}
html,body{width:1200px;height:3922px;overflow:hidden}
body{position:relative;background:var(--board);font-family:"Roboto",sans-serif;color:var(--text)}

.stage{position:absolute;left:0;top:0;width:1200px;height:746px;background:var(--stage);overflow:hidden}
.stage .page{left:355px;top:28px}

.label{position:absolute;width:489px;text-align:center;font-family:"Montserrat",sans-serif;font-weight:600;font-size:21px;letter-spacing:.5px;color:var(--ink)}

.page{position:absolute;width:489px;height:690px;background:var(--white);overflow:hidden;box-shadow:0 2px 6px rgba(0,0,0,.18)}
.wave{position:absolute;left:0;bottom:0;width:489px;height:120px}
.footer{position:absolute;left:18px;right:18px;bottom:10px;display:flex;justify-content:space-between;font-size:6.5px;color:var(--white);letter-spacing:.2px}
.footer b{font-weight:700}
.rule{position:absolute;left:69px;top:0;width:2px;background:var(--sky-deep)}
.title{position:absolute;left:85px;font-family:"Montserrat",sans-serif;font-weight:800;color:var(--heading);font-size:27px;letter-spacing:.3px}
.body{position:absolute;left:85px;right:40px;font-size:6.4px;line-height:1.42;color:var(--text);text-align:justify}
.body p{margin-bottom:7px}

/* Cover */
.cover-top{position:absolute;left:0;top:0;width:489px;height:260px}
.cover-heads{position:absolute;left:0;top:62px;width:489px;text-align:center;color:var(--white);font-family:"Montserrat",sans-serif}
.cover-kicker{font-size:21px;font-weight:400;letter-spacing:.4px}
.cover-title{font-size:38px;font-weight:800;line-height:1.05;letter-spacing:.3px}
.cover-sub{font-family:"Roboto",sans-serif;font-size:15.5px;margin-top:8px;line-height:1.25}
.cover-art{position:absolute;left:70px;top:268px;width:350px;height:250px;border-radius:50%;background:radial-gradient(circle at 50% 55%,#5a6b7c 0 14%,#ffffff 15% 20%,transparent 21%),conic-gradient(from 0deg,var(--art-a),var(--art-b),#f08a3c,#e2527a,#59b35c,var(--art-a));opacity:.85}
.cover-credit{position:absolute;left:0;top:540px;width:489px;text-align:center;font-size:10px;line-height:1.35;color:var(--ink)}
.cover-credit b{font-weight:700;letter-spacing:.2px}
.cover-credit i{display:block}
.cover-year{position:absolute;left:0;top:604px;width:489px;text-align:center;font-family:"Montserrat",sans-serif;font-weight:800;font-size:38px;color:var(--sky-deep)}

/* Credits page */
.credit-by{position:absolute;left:85px;top:157px;font-size:11px;color:var(--ink)}
.credit-name{position:absolute;left:85px;top:172px;font-family:"Montserrat",sans-serif;font-weight:700;font-size:12px;color:var(--heading)}

/* Index */
.toc{position:absolute;left:62px;top:214px;width:370px;font-size:7.2px;color:var(--ink)}
.toc li{list-style:none;display:flex;justify-content:space-between;padding:6px 8px;height:27px;align-items:center}
.toc li:nth-child(odd){background:var(--band-dark)}
.toc li.major{font-weight:700}
.toc-art{position:absolute;left:205px;top:395px;width:215px;height:270px;border-radius:40% 40% 20% 20%;background:linear-gradient(160deg,#c7e6f6,#3276b5 70%,#e9b48f)}

/* Media landscape */
.axis-labels{position:absolute;left:75px;width:370px;font-size:6px;color:var(--sky-deep);font-weight:700;display:flex;justify-content:space-between}
.axis-labels span em{font-style:normal;font-weight:400}
.diagram{position:absolute;left:75px;top:294px;width:370px;height:250px}
.caption{position:absolute;left:0;top:556px;width:489px;text-align:center;font-size:6.4px;font-style:italic;color:var(--ink)}

/* Interviews */
.sub-head{position:absolute;left:85px;font-size:7px;font-weight:700;color:var(--ink)}
.interviews{position:absolute;left:80px;top:262px;width:358px;font-size:6.4px;color:var(--ink)}
.interviews li{list-style:none;padding:6px 6px;min-height:25px;display:flex;align-items:center}
.interviews li:nth-child(even){background:var(--band)}

/* Interview page */
.portrait{position:absolute;left:86px;top:96px;width:83px;height:86px;background:linear-gradient(160deg,#d9b48d,#8a6a4f)}
.person{position:absolute;left:86px;top:192px;font-family:"Montserrat",sans-serif;font-weight:800;font-size:18px;color:var(--heading)}
.person-role{position:absolute;left:86px;top:214px;width:330px;font-size:6.2px;font-style:italic;line-height:1.35}
.quote{position:absolute;left:86px;top:250px;width:340px;font-size:9.8px;line-height:1.4;color:var(--ink);text-align:center;font-weight:500}
.quote .mark{color:var(--heading);font-family:"Montserrat",sans-serif;font-weight:800;font-size:20px;line-height:0;vertical-align:-6px}
.section{font-family:"Montserrat",sans-serif;font-weight:700;color:var(--heading);font-size:8.6px;margin:9px 0 3px}
</style>
</head>
<body>

<section class="stage" aria-label="Report cover">
  <article class="page cover">
    <svg class="cover-top" viewBox="0 0 489 260" preserveAspectRatio="none"><path d="M0 0H489V178C430 150 395 196 330 214C270 232 230 200 160 212C100 222 50 262 0 250Z" fill="var(--sky)"/></svg>
    <div class="cover-heads"><div class="cover-kicker">THE (PRIVATE) NEWS</div><div class="cover-title">SHARING REPORT</div><div class="cover-sub">A starting guide for<br>researchers and journalists</div></div>
    <div class="cover-art" role="img" aria-label="Illustration of a laptop surrounded by connected social sharing icons"></div>
    <div class="cover-credit"><b>A REPORT BY TOMÁS RUIZ ARENAL</b><i>Visiting Scholar at Capitol University (Riverton, USA)</i><i>with the help of Research Grants 18/19 from Southlake University</i><i>of Valdemar (Valdemar, Spain)</i></div>
    <div class="cover-year">2019</div>
  </article>
</section>

<div class="label" style="left:108px;top:828px">COVER PAGE</div>
<div class="label" style="left:615px;top:828px">INNER PAGE 1</div>

<article class="page cover" style="left:108px;top:871px">
  <svg class="cover-top" viewBox="0 0 489 260" preserveAspectRatio="none"><path d="M0 0H489V178C430 150 395 196 330 214C270 232 230 200 160 212C100 222 50 262 0 250Z" fill="var(--sky)"/></svg>
  <div class="cover-heads"><div class="cover-kicker">THE (PRIVATE) NEWS</div><div class="cover-title">SHARING REPORT</div><div class="cover-sub">A starting guide for<br>researchers and journalists</div></div>
  <div class="cover-art" role="img" aria-label="Illustration of a laptop surrounded by connected social sharing icons"></div>
  <div class="cover-credit"><b>A REPORT BY TOMÁS RUIZ ARENAL</b><i>Visiting Scholar at Capitol University (Riverton, USA)</i><i>with the help of Research Grants 18/19 from Southlake University</i><i>of Valdemar (Valdemar, Spain)</i></div>
  <div class="cover-year">2019</div>
</article>

<article class="page" style="left:615px;top:871px">
  <div class="rule" style="left:65px;top:103px;height:84px"></div>
  <div class="credit-by">This is a report by</div>
  <div class="credit-name">TOMÁS RUIZ ARENAL (PHD),</div>
  <div class="body" style="left:65px;top:218px;right:36px;font-size:6.6px">
    <p>a journalist working at Southlake University of Valdemar (SLU, Spain), where he is the Head of the Communication Sciences Department. This project has been supported by a research grant from SLU to do a research stay as a Visiting Scholar at Capitol University (CU), USA, and the help of professor Daniel Hartley at CU.</p>
    <p>Special thanks goes to those who collaborated in the interviews: the journalists at the International Media Fellows Center (IMFC), The Harbor Ledger, Gulf Current Media, Hemisferio, The Civic Accountability Desk, The Iberia Brief, Verifica and Contrasta. In addition, I also want to thank the whole faculty members at the School of Communication at Capitol University, who always offered their collaboration.</p>
    <p>Special thanks also goes to colleagues and scholars who selflessly dedicated their time to talk and hold meetings. They shed light on many topics reflected in the report in depth. They are Ruth Alder, Omar Bashir, Lena Ortiz, Paula Kern, Dana Whitfield, Rafa Lledó, Victor Amsel and Helen Crowe.</p>
    <p>The interviews are expressions of personal opinions as journalists and they do not necessarily express the official point of view of the media where they work. Inquiries for further information about this research can be sent to t.ruiz@slu-mail.example</p>
  </div>
  <svg class="wave" viewBox="0 0 489 120" preserveAspectRatio="none"><path d="M0 40C80 5 150 20 230 55C320 95 410 50 489 18V120H0Z" fill="var(--sky-light)"/><path d="M0 52C90 20 160 40 240 72C330 108 420 70 489 38V120H0Z" fill="var(--sky)"/></svg>
  <div class="footer"><span>THE (PRIVATE) NEWS <b>SHARING REPORT</b></span><span>PAGE - 2</span></div>
</article>

<article class="page" style="left:108px;top:1584px">
  <div class="rule" style="height:183px"></div>
  <div class="title" style="top:154px">INDEX</div>
  <ul class="toc">
    <li class="major"><span>INTRODUCTION</span><span>4</span></li>
    <li class="major"><span>RESEARCH QUESTIONS</span><span>5</span></li>
    <li><span>1. The Media Landscape</span><span>6</span></li>
    <li><span>2. The Interviews</span><span>11</span></li>
    <li><span>3. The Best Practices</span><span>29</span></li>
    <li><span>4. Conclusions</span><span>31</span></li>
    <li><span>5. References</span><span>33</span></li>
  </ul>
  <svg class="wave" viewBox="0 0 489 120" preserveAspectRatio="none"><path d="M0 40C80 5 150 20 230 55C320 95 410 50 489 18V120H0Z" fill="var(--sky-light)"/><path d="M0 52C90 20 160 40 240 72C330 108 420 70 489 38V120H0Z" fill="var(--sky)"/></svg>
  <div class="toc-art" role="img" aria-label="Illustration of a hand holding a smartphone with a person and rating bubbles"></div>
  <div class="footer"><span>THE (PRIVATE) NEWS <b>SHARING REPORT</b></span><span>PAGE - 3</span></div>
</article>

<article class="page" style="left:615px;top:1584px">
  <div class="rule" style="height:145px"></div>
  <div class="title" style="top:118px">INTRODUCTION</div>
  <div class="body" style="top:166px">
    <p>The job of journalists is not just longer on the internet because it ends later, it is also longer because it starts before. On the one hand, a journalist can have a community even before having a journalistic product. On the other hand, social recommendations, incidental consumption of news and online private messages are giving a broader reach to journalism, as we know it now.</p>
    <p>Because publishing is not the end of the journalistic routine, the whole process now is longer. You cannot fully understand what "news" means for people if you do not understand how and why they are sharing the news on online private platforms. Private messaging networks are adding new challenges to journalists and the media. When we are talking about online private environments, issues such as sources, fact-checking, misinformation, privacy or (fake) news are being redefined, as well as the notions of trust, community, public service and media literacy.</p>
    <p>In 2018 the presidential candidate Ricardo Alvim was accused of running a whole fake news campaign through ChatLine with hundreds of millions of messages against his opponent. This scandal is just an example of the growing relevance of fact-checking and the need for media literacy skills among users of private messaging networks.</p>
    <p>Many news sites added a ChatLine sharing option in their news during the last few years (Holt, 2014) and it seems like private channels, such as this one, could become a "major traffic driver for news sites" (Varga, Lind &amp; Moser, 2015: 10). We cannot entirely know what people are doing with news in private messaging networks, but what we can see is what the media and journalists are doing with these platforms. This report is a draft of these actions.</p>
    <p>In news sharing research, a new broad theoretical foundation is needed, with quantitative studies, digital ethnographies or uses and gratifications approaches, and even combining these theories and deriving new ones. We utilize the results of this preliminary research to provide insights so that journalistic practice can be improved, and academic research of journalism can move forward in news sharing research.</p>
    <p>The main goal of this executive report is to help journalists and researchers to get a deeper understanding of the news sharing processes in private messaging apps, channels, and networks. Share it, but not in a private way. Make it as public as you can.</p>
  </div>
  <svg class="wave" viewBox="0 0 489 120" preserveAspectRatio="none"><path d="M0 40C80 5 150 20 230 55C320 95 410 50 489 18V120H0Z" fill="var(--sky-light)"/><path d="M0 52C90 20 160 40 240 72C330 108 420 70 489 38V120H0Z" fill="var(--sky)"/></svg>
  <div class="footer"><span>THE (PRIVATE) NEWS <b>SHARING REPORT</b></span><span>PAGE - 4</span></div>
</article>

<div class="label" style="left:108px;top:2296px">INNER PAGE 2</div>
<div class="label" style="left:615px;top:2296px">INNER PAGE 3</div>

<article class="page" style="left:108px;top:2365px">
  <div class="rule" style="height:145px"></div>
  <div class="title" style="top:118px;font-size:20px">1. THE MEDIA LANDSCAPE</div>
  <div class="body" style="top:150px;left:80px;right:36px">
    <p>If we think about the intersection of the online world and privacy, we can see in the following figure how the last area is the newest and least researched field in journalism, despite its growing influence on issues such as fake news or political communication. As it is said, something does not really go completely viral until it arrives in your personal private messaging networks (ChatLine, Relay, Direct Messages, text messaging, etc.). That is always a sign. There is a paradox here of private journalism, or journalism transmitted and perhaps even created within private messaging services. How do journalists pay attention to this? How could they do it? It would be a kind of journalism based on enabling specific conversations and services to small communities, not just in geographical terms, but communities of interest.</p>
  </div>
  <div class="axis-labels" style="top:286px"><span>1. OFFLINE <em>/ PUBLIC</em></span><span>2. ONLINE <em>/ PUBLIC</em></span></div>
  <svg class="diagram" viewBox="0 0 370 250" aria-label="Four coordinates of communication related to privacy and journalism">
    <g fill="none" stroke="var(--ink)" stroke-width="1.2">
      <rect x="60" y="12" width="240" height="220"/>
      <line x1="180" y1="12" x2="180" y2="232"/>
      <line x1="60" y1="122" x2="300" y2="122"/>
    </g>
    <g font-family="Roboto,sans-serif" font-size="6" font-weight="700" fill="var(--sky-deep)" text-anchor="middle">
      <rect x="150" y="6" width="60" height="10" fill="#fff"/><text x="180" y="14">PUBLIC SIDE</text>
      <rect x="150" y="227" width="60" height="10" fill="#fff"/><text x="180" y="235">PRIVATE SIDE</text>
      <text x="48" y="106">OFFLINE</text>
      <text x="320" y="134">ONLINE</text>
    </g>
    <g fill="var(--sky-deep)">
      <rect x="110" y="38" width="18" height="14" rx="2"/>
      <circle cx="240" cy="44" r="7"/>
      <circle cx="114" cy="148" r="5"/><circle cx="126" cy="148" r="5"/>
      <rect x="232" y="146" width="18" height="14" rx="2"/>
    </g>
    <g font-family="Roboto,sans-serif" font-size="6.2" font-weight="700" fill="var(--ink)" text-anchor="middle">
      <text x="120" y="72">Traditional</text><text x="120" y="80">mass media</text>
      <text x="240" y="72">Online media &amp;</text><text x="240" y="80">social media</text>
      <text x="120" y="180">Offline personal</text><text x="120" y="188">communication</text>
      <text x="240" y="180">Online private messaging</text>
    </g>
    <g font-family="Roboto,sans-serif" font-size="5" fill="var(--ink)" text-anchor="middle">
      <text x="240" y="190">• ChatLine | • SocialChat</text><text x="240" y="198">• Text Messaging | • Relay</text><text x="240" y="206">• Direct Messages</text>
    </g>
  </svg>
  <div class="axis-labels" style="top:536px"><span>3. OFFLINE <em>/ PRIVATE</em></span><span>4. ONLINE <em>/ PRIVATE</em></span></div>
  <div class="caption">Figure 1: The four coordinates of communication related to privacy and journalism</div>
  <svg class="wave" viewBox="0 0 489 120" preserveAspectRatio="none"><path d="M0 40C80 5 150 20 230 55C320 95 410 50 489 18V120H0Z" fill="var(--sky-light)"/><path d="M0 52C90 20 160 40 240 72C330 108 420 70 489 38V120H0Z" fill="var(--sky)"/></svg>
  <div class="footer"><span>THE (PRIVATE) NEWS <b>SHARING REPORT</b></span><span>PAGE - 6</span></div>
</article>

<article class="page" style="left:615px;top:2365px">
  <div class="rule" style="height:145px"></div>
  <div class="title" style="top:118px">THE INTERVIEWS</div>
  <div class="body" style="top:160px;left:82px">
    <p>All the interviews represent the journalists' personal point of view and they are not necessarily the official opinion of the media and institutions where they work. Because of the design of this report, the questions were deleted but you can easily figure out the kind of questions by reading the selected answers.</p>
  </div>
  <div class="sub-head" style="top:244px">INDEX OF INTERVIEWS</div>
  <ul class="interviews">
    <li>1. Clara Westbrook, The International Media Fellows Center, SeedNews Ambassador at the USA.</li>
    <li>2. Marisol Tan, Audience Engagement Editor at The Civic Accountability Desk.</li>
    <li>3. Elena Duarte, Operations Editor at The Harbor Ledger.</li>
    <li>4. Pau Serrat, journalist, Gulf Current Media Network.</li>
    <li>5. Owen Pryce, journalist, The Iberia Brief.</li>
    <li>6. Nuria Campos, digital journalist, Hemisferio Noticias.</li>
    <li>7. Iván Robles, Head of Content at Verifica.</li>
    <li>8. Lucas Ferrer, journalist, Project Consultant at Contrasta.</li>
  </ul>
  <svg class="wave" viewBox="0 0 489 120" preserveAspectRatio="none"><path d="M0 40C80 5 150 20 230 55C320 95 410 50 489 18V120H0Z" fill="var(--sky-light)"/><path d="M0 52C90 20 160 40 240 72C330 108 420 70 489 38V120H0Z" fill="var(--sky)"/></svg>
  <div class="footer"><span>THE (PRIVATE) NEWS <b>SHARING REPORT</b></span><span>PAGE - 5</span></div>
</article>

<div class="label" style="left:108px;top:3102px">INNER PAGE 6</div>
<div class="label" style="left:615px;top:3102px">INNER PAGE 12</div>

<article class="page" style="left:117px;top:3145px">
  <div class="rule" style="height:90px"></div>
  <div class="portrait" role="img" aria-label="Portrait photograph of the interviewee"></div>
  <div class="person">CLARA WESTBROOK</div>
  <div class="person-role">Journalist. The International Media Fellows Center (IMFC), IMFC Fellows &amp; SeedNews Ambassador at the USA</div>
  <div class="quote"><span class="mark">“</span> Media should develop relationships of trust, audience can have a greater sense of trust with messaging privately <span class="mark">”</span></div>
  <div class="body" style="top:288px;left:86px;right:60px">
    <div class="section">FACT-CHECKING AS A MODEL</div>
    <p>Fact-checking is an important component for media organizations to incorporate now and going forward. However, I think that the approach to incorporating fact-checking into news organizations needs to be different for every newsroom. Newsrooms have varying sizes, focuses and specialties, and I do not think that all newsrooms have the capacity to function as fact-checking organizations equally. It is helpful for some news organizations to be the leaders in fact-checking and others can learn from those organizations. For example, Comprobado in Argentina is a pioneer and a resource in regards to fact-checking; not all organizations can fact-check at the deep level that Comprobado does.</p>
    <div class="section">STARTING A JOURNALISTIC PROJECT</div>
    <p>Fact-checking is an important component for media organizations to incorporate now and going forward. However, I think that the approach to incorporating fact-checking into news organizations needs to be different for every newsroom. Newsrooms have varying sizes, focuses and specialties, and I do not think that all newsrooms have the capacity to function as fact-checking organizations equally. It is helpful for some news organizations to be the leaders and a resource for others to learn from.</p>
  </div>
  <svg class="wave" viewBox="0 0 489 120" preserveAspectRatio="none"><path d="M0 40C80 5 150 20 230 55C320 95 410 50 489 18V120H0Z" fill="var(--sky-light)"/><path d="M0 52C90 20 160 40 240 72C330 108 420 70 489 38V120H0Z" fill="var(--sky)"/></svg>
  <div class="footer"><span>THE (PRIVATE) NEWS <b>SHARING REPORT</b></span><span>PAGE - 6</span></div>
</article>

<article class="page" style="left:626px;top:3145px">
  <div class="rule" style="height:150px"></div>
  <div class="body" style="top:168px;left:85px;right:45px">
    <p>Looking for diversified sources of revenue is also an important area in which to develop when starting a digital project on one's own. Putting together a team with diverse strengths will also help with finding different revenue sources and having a solid project overall. For example, at SeedNews, we like to remind people that they should probably not start an independent media organization with a team exclusively comprised of reporters. In addition to those journalists, there should be someone with more experience in business/finance, so that someone on the team is able to help guide everyone on how to run the media organization as a business.</p>
    <div class="section">PRIVATE NETWORKS</div>
    <p>Private networks are something that media organizations all over the world are exploring, especially organizations with niche audiences or organizations trying to reach audiences where misinformation spreads rapidly.</p>
    <div class="section">TEACHING MEDIA LITERACY</div>
    <p>I do think media organizations have a role to play as far as teaching their audiences media literacy. While I do not think many audience members will want to take the time to fact-check information themselves, I think media organizations should develop relationships of trust with their audience members. If there is trust between a media organization and its audience, the audience will feel more comfortable coming to journalists with questions and will be receptive to fact-checked information from that media organization.</p>
    <div class="section">MORE TRUST</div>
    <p>I do think media organizations have a role to play as far as teaching their audiences media literacy. While I do not think many audience members will want to take the time to fact-check information themselves, I think media organizations should develop relationships of trust with their audience members, so the audience will be receptive to fact-checked information.</p>
  </div>
  <svg class="wave" viewBox="0 0 489 120" preserveAspectRatio="none"><path d="M0 40C80 5 150 20 230 55C320 95 410 50 489 18V120H0Z" fill="var(--sky-light)"/><path d="M0 52C90 20 160 40 240 72C330 108 420 70 489 38V120H0Z" fill="var(--sky)"/></svg>
  <div class="footer"><span>THE (PRIVATE) NEWS <b>SHARING REPORT</b></span><span>PAGE - 7</span></div>
</article>

<div class="label" style="left:117px;top:3868px">INNER PAGE 13</div>
<div class="label" style="left:626px;top:3868px">INNER PAGE 14</div>

</body>
</html>
```